Vorlund Business Card Design Needed

We are a consultation firm called "Vorlund Inc" or simply Vorlund. Would would like a simple card utilizing the blue and grays in our logo (perhaps even different shades and hues of blue). Logo and Initials of Card holder one side and information on the other.

Target Market(s)

We are B 2 B company. We deal mostly with upper management.

Industry/Entity Type

Business

Contact Information for Business Card

Name. Title. phone. email. website.

```html
<!DOCTYPE html>
<html lang="en">
<head>
<meta charset="utf-8">
<title>Vorlund Business Card</title>
<link href="https://fonts.googleapis.com/css2?family=Source+Sans+3:wght@400;600;700&display=swap" rel="stylesheet">
<style>
  :root {
    --backdrop: #3a332f;
    --card-black: #151516;
    --card-edge: #232325;
    --brand-blue: #1e8fd8;
    --silver: #b9bcbf;
    --text-light: #e6e7e8;
    --text-muted: #a7a9ac;
  }
  * { margin: 0; padding: 0; box-sizing: border-box; }
  html, body { width: 1200px; height: 779px; overflow: hidden; }
  body {
    background: var(--backdrop);
    font-family: "Source Sans 3", "Source Sans Pro", sans-serif;
    display: flex;
    align-items: center;
    justify-content: center;
    gap: 40px;
  }
  .card {
    width: 540px;
    height: 309px;
    background: var(--card-black);
    border: 1px solid var(--card-edge);
    border-radius: 4px;
    box-shadow: 0 10px 30px rgba(0,0,0,0.45);
    position: relative;
  }
  /* Back side: brand name only */
  .card-back {
    display: flex;
    align-items: center;
    justify-content: center;
    gap: 18px;
  }
  .brand-dot {
    width: 34px; height: 34px; border-radius: 50%;
    border: 3px solid var(--silver);
  }
  .brand-name {
    font-weight: 700;
    font-size: 52px;
    letter-spacing: 1px;
  }
  .card-back .brand-name { color: var(--silver); }
  /* Front side: brand + contact info */
  .card-front {
    display: flex;
    align-items: center;
    padding: 0 34px 0 36px;
  }
  .front-brand {
    width: 200px;
    display: flex;
    align-items: center;
    gap: 12px;
  }
  .front-brand .brand-dot { width: 24px; height: 24px; border-color: var(--brand-blue); }
  .front-brand .brand-name { color: var(--brand-blue); font-size: 36px; }
  .contact-block { margin-left: 40px; }
  .holder-name {
    color: var(--brand-blue);
    font-weight: 700;
    font-size: 26px;
    line-height: 1;
  }
  .holder-title {
    color: var(--text-muted);
    font-size: 14px;
    margin-top: 3px;
  }
  .address {
    color: var(--text-light);
    font-size: 14px;
    line-height: 1.3;
    margin-top: 16px;
  }
  .contact-list {
    list-style: none;
    margin-top: 16px;
    color: var(--text-light);
    font-size: 14px;
    line-height: 1.45;
  }
  .contact-list li { display: flex; align-items: center; gap: 8px; }
  .contact-icon { width: 11px; height: 11px; fill: var(--brand-blue); flex: none; }
</style>
</head>
<body>
  <section class="card card-back" aria-label="Card back">
    <span class="brand-dot"></span>
    <span class="brand-name">Vorlund</span>
  </section>

  <section class="card card-front" aria-label="Card front">
    <div class="front-brand">
      <span class="brand-dot"></span>
      <span class="brand-name">Vorlund</span>
    </div>
    <div class="contact-block">
      <h1 class="holder-name">Daniel Marsh</h1>
      <p class="holder-title">Managing Member</p>
      <p class="address">2210 Harbor Lane,<br>Fairview, CA 95014</p>
      <ul class="contact-list">
        <li><svg class="contact-icon" viewBox="0 0 12 12"><path d="M2.5 0.5 L4.5 0.5 L5.2 3.3 L3.8 4.4 Q5 7 7.6 8.2 L8.7 6.8 L11.5 7.5 L11.5 9.5 Q11.5 11.5 9.5 11.5 Q0.5 10.5 0.5 2.5 Q0.5 0.5 2.5 0.5 Z"/></svg>(555) 201-4410</li>
        <li><svg class="contact-icon" viewBox="0 0 12 12"><rect x="3" y="0.5" width="6" height="3"/><rect x="0.5" y="4" width="11" height="5" rx="1"/><rect x="3" y="8" width="6" height="3.5"/></svg>(555) 201-4411</li>
        <li><svg class="contact-icon" viewBox="0 0 12 12"><path d="M3 0.5 H9 V11.5 H3 Z M4 1.5 V9 H8 V1.5 Z"/></svg>(555) 388-9120</li>
        <li><svg class="contact-icon" viewBox="0 0 12 12"><path d="M0.5 2 H11.5 V10 H0.5 Z M1.5 3 L6 6.5 L10.5 3 Z"/></svg>daniel@vorlund.example</li>
        <li><svg class="contact-icon" viewBox="0 0 12 12"><circle cx="6" cy="6" r="5.5"/></svg>www.vorlund.example</li>
      </ul>
    </div>
  </section>
</body>
</html>
```